Security doors and flyscreens

We need business cards for our company called K & M Distributors. We quote, manufacture and install security doors and flyscreens.

Industry/Entity Type

Security

Contact Information for Business Card

K & M DISTRIBUTORS
17 Larkvale Rd. Ashgrove 3091
Ph: 8157 2604
Fax: 8157 2609
Gavin: 0419 275 916
Email: gatesupplier@mailbox-example.net

```html
<!DOCTYPE html>
<html lang="en">
<head>
<meta charset="utf-8">
<title>K &amp; M Distributors – Business Card</title>
<link rel="stylesheet" href="https://fonts.googleapis.com/css2?family=Cinzel:wght@400;700&family=Roboto+Condensed:wght@400;700&family=Questrial&display=swap">
<style>
  :root {
    --navy: #0b0c45;
    --gold: #d4a23a;
    --grey: #9a9a9a;
    --ink: #555a66;
    --paper: #ffffff;
    --backdrop: #e6e4e0;
    --ghost: #eef0f6;
  }
  * { margin: 0; padding: 0; box-sizing: border-box; }
  html, body { width: 1200px; height: 800px; overflow: hidden; }
  body { background: var(--backdrop); position: relative; }

  .card {
    position: absolute; left: 50px; top: 69px;
    width: 1100px; height: 662px;
    background: var(--paper);
    border-radius: 16px;
    overflow: hidden;
    box-shadow: 0 6px 18px rgba(0,0,0,.18);
  }
  .ghost-mark {
    position: absolute; left: 694px; top: 0; width: 406px; height: 411px;
    background: var(--ghost); opacity: .6;
  }
  .brand-mark {
    position: absolute; left: 54px; top: 40px; width: 224px; height: 267px;
    display: flex; align-items: center; justify-content: center;
    font-family: "Cinzel", serif; font-weight: 700; font-size: 64px;
    color: var(--navy); letter-spacing: 2px;
  }
  .company-name {
    position: absolute; left: 333px; top: 50px; width: 690px;
    font-family: "Cinzel", serif; font-weight: 400; font-size: 88px;
    line-height: 1; color: var(--navy); white-space: nowrap;
  }
  .tagline {
    position: absolute; left: 357px; top: 150px; width: 650px;
    font-family: "Cinzel", serif; font-weight: 700; font-size: 21px;
    line-height: 1.35; color: var(--gold); text-transform: uppercase;
    text-align: center;
  }
  .rule {
    position: absolute; left: 270px; right: 0; top: 222px; height: 6px;
    background: var(--navy);
  }
  .person {
    position: absolute; left: 40px; top: 350px; width: 444px;
    font-family: "Roboto Condensed", sans-serif; text-align: right;
  }
  .person-name { font-size: 76px; line-height: 1; font-weight: 400; color: var(--gold); white-space: nowrap; }
  .person-name b { font-weight: 700; color: var(--navy); }
  .person-role { font-size: 44px; font-weight: 700; color: var(--grey); line-height: 1.05; }

  .contact {
    position: absolute; left: 622px; top: 278px; list-style: none;
    font-family: "Questrial", sans-serif; font-size: 23px; color: var(--ink);
  }
  .contact li { display: flex; align-items: flex-start; line-height: 36px; white-space: nowrap; }
  .contact li.gap { margin-top: 8px; }
  .contact .icon { width: 26px; height: 36px; flex: none; display: flex; align-items: center; justify-content: center; margin-right: 12px; }
  .contact .icon svg { width: 22px; height: 22px; fill: var(--gold); }
  .contact .indent { padding-left: 38px; }

  .swoosh { position: absolute; left: 0; top: 0; width: 1100px; height: 662px; }
</style>
</head>
<body>
  <div class="card">
    <div class="ghost-mark" aria-hidden="true"></div>

    <div class="brand-mark">K &amp; M</div>
    <h1 class="company-name">DISTRIBUTORS</h1>
    <p class="tagline">Manufacture and install security doors<br>and flyscreens.</p>
    <div class="rule"></div>

    <div class="person">
      <div class="person-name"><b>NAME</b> SAMPLE</div>
      <div class="person-role">POSITION</div>
    </div>

    <ul class="contact">
      <li><span class="icon"><svg viewBox="0 0 24 24"><path d="M12 2a7 7 0 0 0-7 7c0 5 7 13 7 13s7-8 7-13a7 7 0 0 0-7-7zm0 9.5A2.5 2.5 0 1 1 12 6.5a2.5 2.5 0 0 1 0 5z"/></svg></span>17 Larkvale Rd. Ashgrove</li>
      <li class="indent">3091</li>
      <li class="gap"><span class="icon"><svg viewBox="0 0 24 24"><path d="M7 1h10a2 2 0 0 1 2 2v18a2 2 0 0 1-2 2H7a2 2 0 0 1-2-2V3a2 2 0 0 1 2-2zm0 3v14h10V4z"/></svg></span>8157 2604</li>
      <li><span class="icon"><svg viewBox="0 0 24 24"><path d="M2 6h20v14H2zM5 10v2h14v-2zm0 4v2h9v-2z"/></svg></span>Fax:8157 2609</li>
      <li><span class="icon"><svg viewBox="0 0 24 24"><path d="M2 3h20v14H2zm2 2v10h16V5zM9 19h6v2H9z"/></svg></span>Gavin:0419 275 916</li>
      <li class="indent">gatesupplier@mailbox-example.net</li>
    </ul>

    <svg class="swoosh" viewBox="0 0 1100 662" aria-hidden="true">
      <path d="M318,597 C650,590 900,548 1100,494 L1100,520 C900,576 650,600 318,597 Z" fill="var(--gold)"/>
      <path d="M0,497 C120,560 260,598 500,604 C750,610 950,596 1100,566 L1100,662 L0,662 Z" fill="var(--navy)"/>
    </svg>
  </div>
</body>
</html>
```